A paperback book cover entitled: The Lantern

1. For the front cover of the paperback I need the photo of me walking down the driveway at Larkspur Hall as the focal point. The designer will use their discretion where to insert the book title: The Lantern.
Also the designer will use their discretion where my name Gregor Tennant as the author is placed. Attached is a contemporary photo of me to use if the designer thinks that possible. Both these photos are attached.
2. The back cover page will contain two main written insertions (1) About the Book and (2) About the Author.
The book will be an 8.5x11 inch paperback of some 570 pages published by Bookvale.
About the book:
This book is about Australian Public Affairs 1957-2020 as perceived and observed by Gregor Tennant. It has a significant but not exclusive Queensland focus concerning History, Commentary, and Anecdotes, plus some things Gregor has been involved with along the way.
Gregor developed unique Transition to Government and Transition to Opposition plans that have all been implemented. Some of those plans are referred to in the book and other Transition plans are appendixes to the book.
Now at 73 years of age, Gregor’s motivation for writing this book is to ensure a wealth of historical scenarios are captured and incorporated into the public record for future generations.

About the author:

Gregor Tennant has been a largely silent and invisible political confidant to Australian Premiers and Prime Ministers.
Gregor worked in the Queensland public sector from 1971-2009 as Chief of Staff to four Queensland State Opposition Leaders for 13 years and then as a Public Sector senior executive.
He subsequently served on the Edith Quarrie Foundation Board, the Harwood Reading Institute Board, and consulted to a mining company. He has recorded many Oral History projects for The Corben Archive in Canberra.
Over the last 30+ years, he has been approached countless times for advice relating to Business, Government, Authors, Historians, and people seeking a job. He has never charged a cent for any of his advice, even when not working within Government.
There are two extra photos attached to maybe be on each side at the bottom of the back cover if the designer thinks it is appropriate.
Those in the 4 person photo from the left were all connected with the Tamberlin Assembly: former Unity Minister Neil Ostrand, Former Frontier Party Premier Rod Vesey, former Civic Leader Barry Lund, and Gregor Tennant

In the three person photo from the left are: Gregor Tennant, Former PM Clive Fennimore, and Prime Minister Dean Parrow.

3. In the spine of the book will be simply (1) The Lantern and (2) Gregor Tennant

Here’s hoping a good design is created.

```html
<!DOCTYPE html>
<html lang="en">
<head>
<meta charset="utf-8">
<title>The Lantern — Cover Wrap</title>
<link rel="stylesheet" href="https://fonts.googleapis.com/css2?family=Barlow+Condensed:wght@400;500;600&family=Barlow+Semi+Condensed:wght@500&display=swap">
<style>
  :root {
    --ink: #000000;
    --paper: #ffffff;
    --gold: #f2d593;
    --gold-bar: #efdaa4;
    --photo-light: #c9c9c9;
    --photo-mid: #8a8a8a;
    --photo-dark: #3a3a3a;
    --body-font: "Barlow Condensed", "Arial Narrow", sans-serif;
    --name-font: "Barlow Semi Condensed", "Arial Narrow", sans-serif;
  }
  * { box-sizing: border-box; margin: 0; padding: 0; }
  html, body {
    width: 1200px; height: 1200px; overflow: hidden;
    background: var(--paper);
  }
  .cover-wrap {
    position: absolute; left: 18px; top: 234px;
    width: 1164px; height: 731px;
    background: var(--ink);
    overflow: hidden;
  }

  /* Back cover */
  .back-cover {
    position: absolute; left: 52px; top: 0; width: 463px;
    color: var(--paper);
    font-family: var(--body-font);
    font-weight: 400;
  }
  .section-heading {
    position: absolute; left: 0; width: 463px;
    display: flex; align-items: center; gap: 16px;
    color: var(--gold);
    font-family: var(--body-font);
    font-weight: 500;
    font-size: 22px;
    letter-spacing: 0.3px;
    white-space: nowrap;
  }
  .section-heading::before,
  .section-heading::after {
    content: ""; flex: 1; height: 1px; background: var(--paper);
  }
  .heading-book { top: 30px; }
  .heading-author { top: 265px; }

  .book-blurb {
    position: absolute; left: 0; top: 77px; width: 463px;
    font-size: 12.4px; line-height: 18.75px; text-align: justify;
  }
  .book-blurb p + p { margin-top: 6.5px; }

  .author-bio {
    position: absolute; left: 0; top: 312px; width: 463px;
    font-size: 10.6px; line-height: 14.8px; text-align: justify;
  }
  .author-bio p + p { margin-top: 6.3px; }

  .author-figure {
    float: left; width: 112px; margin: 7px 17px 4px 0;
  }
  .author-figure .photo {
    width: 112px; height: 87px;
    background: linear-gradient(135deg, #c8a45c 0%, #6b5632 45%, #d9cfbf 100%);
  }
  .author-figure figcaption {
    margin-top: 9px;
    font-size: 6.3px; line-height: 10px; font-weight: 600;
    text-align: left;
  }
  .author-figure .caption-lead { color: var(--gold); display: block; }

  /* Spine */
  .spine-title,
  .spine-author {
    position: absolute; left: 574px;
    writing-mode: vertical-rl;
    font-family: var(--body-font);
    font-size: 13px;
    letter-spacing: 11.5px;
    white-space: nowrap;
  }
  .spine-title { top: 46px; color: var(--paper); z-index: 3; }
  .spine-author { top: 387px; color: var(--gold); z-index: 3; }

  /* Front cover */
  .front-photo {
    position: absolute; left: 566px; top: 0; width: 598px; height: 731px;
    background:
      radial-gradient(ellipse 30% 55% at 52% 62%, var(--photo-dark) 0%, rgba(58,58,58,0) 70%),
      linear-gradient(180deg, #5a5a5a 0%, #7e7e7e 30%, var(--photo-light) 55%, #a9a9a9 80%, #8f8f8f 100%);
  }
  .spine-foot {
    position: absolute; left: 566px; top: 331px; width: 33px; height: 400px;
    background: var(--ink);
  }
  .gold-bar {
    position: absolute; left: 1079px; top: 0; width: 55px; height: 328px;
    background: var(--gold-bar);
  }
  .author-portrait {
    position: absolute; left: 1079px; top: 328px; width: 55px; height: 72px;
    background: linear-gradient(180deg, #d6d6d6 0%, #9a9a9a 55%, #2c3346 100%);
  }
  .black-bar {
    position: absolute; left: 1079px; top: 566px; width: 55px; height: 165px;
    background: var(--ink);
  }
  .author-band {
    position: absolute; left: 905px; top: 400px; width: 259px; height: 52px;
    background: var(--ink);
    display: flex; align-items: center; justify-content: flex-end;
    padding-right: 30px;
    color: var(--gold);
    font-family: var(--name-font);
    font-weight: 500;
    font-size: 29px;
    letter-spacing: 1.2px;
    z-index: 2;
  }
  .front-title {
    position: absolute; left: 0; top: 0; width: 1164px; height: 731px;
    z-index: 1;
  }
  .front-title text {
    font-family: var(--body-font);
    font-weight: 400;
    fill: var(--paper);
  }
</style>
</head>
<body>
  <main class="cover-wrap">

    <section class="back-cover">
      <h2 class="section-heading heading-book">ABOUT THE BOOK</h2>
      <div class="book-blurb">
        <p>This book is about Australian Public Affairs 1957-2020 as perceived and observed by Gregor Tennant. It has a significant but not exclusive Queensland focus concerning History, Commentary, and Anecdotes, plus some things Gregor has been involved with along the way.</p>
        <p>Gregor developed unique Transition to Government and Transition to Opposition plans that have all been implemented. Some of those plans are referred to in the book and other Transition plans are appendixes to the book.</p>
        <p>Now at 73 years of age, Gregor’s motivation for writing this book is to ensure a wealth of historical scenarios are captured and incorporated into the public record for future generations.</p>
      </div>

      <h2 class="section-heading heading-author">ABOUT THE AUTHOR</h2>
      <div class="author-bio">
        <figure class="author-figure">
          <div class="photo" role="img" aria-label="Photo of Gregor Tennant with former PM Clive Fennimore and Prime Minister Dean Parrow"></div>
          <figcaption><span class="caption-lead">From left :</span>Gregor Tennant, Former PM Clive Fennimore, and Prime Minister Dean Parrow.</figcaption>
        </figure>
        <p>Gregor Tennant has been a largely silent and invisible political confidant to Australian Premiers and Prime Ministers.</p>
        <p>Gregor worked in the Queensland public sector from 1971-2009 as Chief of Staff to four Queensland State Opposition Leaders for 13 years and then as a Public Sector senior executive.</p>
        <p>He subsequently served on the Edith Quarrie Foundation Board, the Harwood Reading Institute Board, and consulted to a mining company. He has recorded many Oral History projects for The Corben Archive in Canberra.</p>
        <p>Over the last 30+ years, he has been approached countless times for advice relating to Business, Government, Authors, Historians, and people seeking a job. He has never charged a cent for any of his advice, even when not working within Government.</p>
        <p>There are two extra photos attached to maybe be on each side at the bottom of the back cover if the designer thinks it is appropriate.</p>
        <p>Those in the 4 person photo from the left were all connected with the Tamberlin Assembly: former Unity Minister Neil Ostrand, Former Frontier Party Premier Rod Vesey, former Civic Leader Barry Lund, and Gregor Tennant.</p>
      </div>
    </section>

    <div class="front-photo" role="img" aria-label="Black and white photo of Gregor Tennant walking down the driveway at Larkspur Hall"></div>
    <div class="spine-foot"></div>
    <div class="spine-title">THE LANTERN</div>
    <div class="spine-author">GREGOR TENNANT</div>

    <div class="gold-bar"></div>
    <div class="author-portrait" role="img" aria-label="Contemporary portrait of Gregor Tennant"></div>
    <div class="black-bar"></div>

    <svg class="front-title" viewBox="0 0 1164 731" aria-label="The Lantern">
      <rect x="625" y="360" width="175" height="24" fill="#ffffff" opacity="0.14"/>
      <rect x="716" y="452" width="448" height="12" fill="#000000" opacity="0.18"/>
      <rect x="716" y="545" width="448" height="20" fill="#ffffff" opacity="0.12"/>
      <rect x="716" y="353" width="14" height="100" fill="#ffffff"/>
      <text x="625" y="439" font-size="158" textLength="158" lengthAdjust="spacingAndGlyphs">THE</text>
      <text x="716" y="563" font-size="158" textLength="417" lengthAdjust="spacingAndGlyphs">LANTERN</text>
    </svg>

    <div class="author-band">GREGOR TENNANT</div>
  </main>
</body>
</html>
```